KRV e-payment Business Card Design

We require a new business card design to suit our expanding consulting business -who are specialists in 2 main areas
1. Advising large Corporations and Government organisation on how to improve the why they use emerging (B2B) electronic payment systems
2. Educate Global and regional banks on how to design, build and market electronic business payment products in emerging markets

Our logo is grey/silver based with a building block theme. It also suggests "insight" and business know-how capitalizing on our KRV name. We also want to engender trust,security and balance via the ying/yan symbol

The design needs to take into account the target regional areas of Australiasia/Asia Pacific/Middle East and Africa

Target Market(s)

Regional Banks and their business customers

Industry/Entity Type

Electronic

Contact Information for Business Card

Marcus Delwyn
Director KRV Consulting (Aust) Pty Ltd
PO Box 7463
Brookvale NSW 2175
Australia
tel +61 (0) 2 95550417
mob +61 (0) 455503862
krvconsulting@tallwire.example

```html
<!DOCTYPE html>
<html lang="en">
<head>
<meta charset="utf-8">
<title>KRV e-payment Business Card</title>
<link rel="stylesheet" href="https://fonts.googleapis.com/css2?family=Questrial&family=Dancing+Script:wght@600&family=EB+Garamond:ital@1&display=swap">
<style>
  :root {
    --backdrop: #d9d9d9;
    --card-light: #fafafa;
    --card-mid: #e6e6e6;
    --ink: #111111;
    --mark-dot: #9a9a9a;
  }
  html, body {
    margin: 0;
    padding: 0;
    width: 1200px;
    height: 1200px;
    overflow: hidden;
    background: var(--backdrop);
  }
  p, h1, dl { margin: 0; }
  .canvas {
    width: 1200px;
    height: 1200px;
    display: flex;
    flex-direction: column;
    align-items: center;
    justify-content: center;
    gap: 40px;
  }
  .card {
    position: relative;
    width: 960px;
    height: 540px;
    background: radial-gradient(ellipse at 50% 40%, var(--card-light) 0%, var(--card-mid) 100%);
    box-shadow: 0 6px 18px rgba(0,0,0,0.18);
    font-family: "Questrial", sans-serif;
    color: var(--ink);
    overflow: hidden;
  }
  .brand {
    position: absolute;
    display: flex;
    align-items: center;
    gap: 14px;
  }
  .brand-name {
    font-family: "Questrial", sans-serif;
    color: var(--ink);
    letter-spacing: 0.08em;
  }
  .brand-dot {
    border-radius: 50%;
    background: var(--mark-dot);
  }
  .tagline,
  .company-line {
    position: absolute;
    font-family: "EB Garamond", serif;
    font-style: italic;
    color: var(--ink);
    white-space: nowrap;
  }

  /* back side */
  .card-back .brand { left: 110px; top: 70px; }
  .card-back .brand-name { font-size: 48px; }
  .card-back .brand-dot { width: 22px; height: 22px; }
  .card-back .tagline { left: 110px; top: 150px; font-size: 15px; }
  .card-back .company-line { left: 290px; top: 140px; font-size: 15px; }
  .address {
    position: absolute;
    left: 90px;
    top: 330px;
    font-size: 19px;
    line-height: 1.3;
  }
  .divider {
    position: absolute;
    left: 500px;
    top: 80px;
    width: 2px;
    height: 250px;
    background: var(--ink);
  }
  .person {
    position: absolute;
    right: 70px;
    top: 70px;
    width: 300px;
  }
  .person-name {
    font-family: "Dancing Script", cursive;
    font-weight: 600;
    font-size: 38px;
    border-bottom: 2px solid var(--ink);
    padding-bottom: 2px;
  }
  .person-role {
    font-family: "Dancing Script", cursive;
    font-size: 20px;
    margin: 4px 0 0 6px;
  }
  .contact {
    position: absolute;
    left: 530px;
    top: 370px;
    display: grid;
    grid-template-columns: 84px auto;
    row-gap: 2px;
    font-size: 20px;
  }
  .contact dt { font-weight: bold; }
  .contact dd { margin: 0; }

  /* front side */
  .card-front .brand { left: 130px; top: 150px; }
  .card-front .brand-name { font-size: 110px; }
  .card-front .brand-dot { width: 44px; height: 44px; }
  .card-front .tagline { left: 130px; top: 300px; font-size: 22px; }
  .card-front .company-line { left: 410px; top: 296px; font-size: 24px; }
</style>
</head>
<body>
<main class="canvas">
  <section class="card card-back" aria-label="Card back">
    <div class="brand">
      <span class="brand-name">KRV</span>
      <span class="brand-dot"></span>
    </div>
    <p class="tagline">“clear payment foresight”</p>
    <p class="company-line">Consulting (Australia) Pty Ltd</p>
    <p class="address">KRV Consulting (Aust) Pty Ltd<br>PO Box 7463 Brookvale NSW 2175 Australia</p>
    <div class="divider"></div>
    <div class="person">
      <h1 class="person-name">Marcus Delwyn</h1>
      <p class="person-role">-Director</p>
    </div>
    <dl class="contact">
      <dt>Tel:</dt><dd>+61 (0) 2 95550417</dd>
      <dt>Mob:</dt><dd>+61 (0) 455503862</dd>
      <dt>Email:</dt><dd>krvconsulting@tallwire.example</dd>
    </dl>
  </section>

  <section class="card card-front" aria-label="Card front">
    <div class="brand">
      <span class="brand-name">KRV</span>
      <span class="brand-dot"></span>
    </div>
    <p class="tagline">“clear payment foresight”</p>
    <p class="company-line">Consulting (Australia) Pty Ltd</p>
  </section>
</main>
</body>
</html>
```